HTML newsletter template for construction company

Hello. I need a company newsletter template made. Our website is: www.harrowmintwork.com

Can you please spend some time on our website and design a similarly themed newsletter template for us? We use infusionsoft, so it'd be great if someone has experience with infusionsoft's newsletter requirements.

Target Market(s)

All sized subcontracting companies. We are a national company but are headquartered in Phoenix, Az.

Industry/Entity Type

Construction Company

Font styles to use
Sans Serif

Requirements
Must have
• html
Nice to have
• We need a few different "sections" for content. We're planning on having an interview, a construction project spotlight, some type of article, tips of some-sort and provide a few upcoming events that we are participating in.

```html
<!DOCTYPE html>
<html lang="en">
<head>
<meta charset="utf-8">
<title>Harrowmint Work Newsletter</title>
<link href="https://fonts.googleapis.com/css2?family=Roboto:wght@400;500;700&display=swap" rel="stylesheet">
<style>
:root{
  --sky:#5ea8ee;
  --blue:#4a8fd6;
  --orange:#e8541e;
  --event-1:#f58a4f;
  --event-2:#f2621e;
  --event-3:#c9440f;
  --ink:#4a4f55;
  --muted:#6c737a;
  --pale:#f1f5f9;
  --pale-blue:#dbe9f6;
  --footer:#262a2f;
  --footer-deep:#1d2024;
  --footer-text:#aeb4ba;
  --white:#ffffff;
}
*{margin:0;padding:0;box-sizing:border-box}
html,body{width:1200px;height:2984px;overflow:hidden;background:var(--white)}
body{font-family:'Roboto',Arial,sans-serif;color:var(--ink);position:relative}
.abs{position:absolute}

.topbar{position:absolute;left:0;top:0;width:1200px;height:119px;background:var(--sky);
  display:flex;align-items:center;justify-content:center;color:var(--white);font-size:27px;gap:28px}

.contact-row{position:absolute;left:0;top:119px;width:1200px;height:234px}
.label-blue{color:var(--blue);font-weight:700;font-size:38px}
.phone-big{color:var(--orange);font-weight:500;font-size:40px}
.social-dot{width:59px;height:59px;border-radius:50%;background:var(--orange);display:inline-block;margin-right:10px}

.hero{position:absolute;left:0;top:353px;width:1200px;height:695px;
  background:linear-gradient(135deg,#3b3026 0%,#6d5134 40%,#a8845c 70%,#4e3e2e 100%);text-align:center;color:var(--white)}
.hero-shade{position:absolute;inset:0;background:rgba(20,18,16,.45)}
.brand-mark{position:absolute;left:510px;top:65px;width:180px;height:180px;border-radius:50%;background:#2b2b2b}
.brand-name{position:absolute;left:0;width:1200px;top:290px;font-size:52px;font-weight:400}
.hero-title{position:absolute;left:0;width:1200px;top:418px;font-size:60px;font-weight:700}
.btn{display:flex;align-items:center;justify-content:center;background:var(--orange);color:var(--white);border-radius:6px}
.hero .btn{position:absolute;left:429px;top:544px;width:339px;height:85px;font-size:36px}

.spotlight-photo{position:absolute;left:13px;top:1088px;width:574px;height:389px;border:8px solid #2a2a2a;
  background:linear-gradient(180deg,#3e74c4 0%,#6b9ad8 45%,#c9a56a 80%,#5a4a3a 100%)}
.section-title-orange{color:var(--orange);font-weight:700;font-size:48px}
.body-copy{font-size:26px;line-height:40px;color:var(--ink)}
.btn-small{position:absolute;height:60px;font-size:27px;border-radius:4px}

.tips{position:absolute;left:0;top:1556px;width:1200px;height:462px;background:var(--pale)}
.section-title-grey{position:absolute;left:0;width:1200px;text-align:center;font-weight:700;font-size:48px;color:#555b61}

.events-head{position:absolute;left:0;top:2037px;width:1200px;height:90px;background:var(--pale-blue)}
.event{position:absolute;top:2146px;height:201px;color:var(--white);padding:28px 0 0 36px}
.event h3{font-size:36px;font-weight:700;margin-bottom:10px}
.event p{font-size:29px;line-height:40px;font-weight:500}

.press{position:absolute;left:0;top:2397px;width:1200px;height:168px;border-top:3px solid #d6d9dc;border-bottom:3px solid #d6d9dc;
  display:flex;align-items:center;justify-content:space-around}
.press-badge{width:230px;height:60px;background:#c9cdd1;border-radius:4px}

.footer{position:absolute;left:0;top:2614px;width:1200px;height:370px;background:var(--footer);color:var(--footer-text)}
.footer .label{color:var(--white);font-size:28px;font-weight:500}
.footer .value{font-size:28px;line-height:56px}
.follow-bar{position:absolute;left:0;top:297px;width:1200px;height:73px;background:var(--footer-deep);border-top:2px solid #3a3f45;
  display:flex;align-items:center;justify-content:center;gap:34px;color:var(--white);font-size:28px;font-weight:500}
.follow-bar .dot{width:32px;height:32px;background:var(--white);border-radius:50%}
</style>
</head>
<body>

<header class="topbar"><span>View in Web Browser</span><span>|</span><span>Forward to Your Friend</span></header>

<section class="contact-row">
  <div class="abs label-blue" style="left:33px;top:60px">CALL US:</div>
  <div class="abs phone-big" style="left:33px;top:114px">+1 (866) 555-0142</div>
  <div class="abs label-blue" style="left:785px;top:60px">FOLLOW US</div>
  <div class="abs" style="left:790px;top:118px">
    <span class="social-dot"></span><span class="social-dot"></span><span class="social-dot"></span><span class="social-dot"></span><span class="social-dot"></span>
  </div>
</section>

<section class="hero" role="img" aria-label="Photo of a contractor in a hard hat reviewing plans inside a timber house frame">
  <div class="hero-shade"></div>
  <div class="brand-mark"></div>
  <div class="brand-name">Harrowmint Work</div>
  <h1 class="hero-title">WE FUND CONTRACTORS</h1>
  <div class="btn">Apply Now</div>
</section>

<section class="spotlight">
  <div class="spotlight-photo" role="img" aria-label="Photo of a modern glass office building lit at dusk"></div>
  <h2 class="abs section-title-orange" style="left:620px;top:1098px">PROJECT SPOTLIGHT</h2>
  <p class="abs body-copy" style="left:620px;top:1180px;width:555px">lorel ipsum dolor sit amet esta di marai aninuo alencia lorel ipsum dolor sit amet esta di marai aninuo alenciaiorel ipsum dolor sit amet esta di marai aninuo alencia</p>
  <div class="btn btn-small" style="left:627px;top:1399px;width:211px">Read More</div>
</section>

<section class="tips">
  <h2 class="section-title-grey" style="top:30px">TIPS &amp; TECHNIQUES</h2>
  <p class="abs body-copy" style="left:33px;top:140px;width:540px">lorel ipsum dolor sit amet esta di marai aninuo alencia lorel ipsum dolor sit amet esta di marai aninuo alenciaIorel ipsum dolor sit amet esta di marai aninuo alencia</p>
  <p class="abs body-copy" style="left:637px;top:140px;width:540px">lorel ipsum dolor sit amet esta di marai aninuo alencia lorel ipsum dolor sit amet esta di marai aninuo alenciaIorel ipsum dolor sit amet esta di marai aninuo alencia</p>
  <div class="btn btn-small" style="left:36px;top:364px;width:179px">Read More</div>
  <div class="btn btn-small" style="left:643px;top:364px;width:179px">Read More</div>
</section>

<section class="events-head">
  <h2 class="section-title-grey" style="top:16px">UPCOMING EVENTS</h2>
</section>
<div class="event" style="left:0;width:389px;background:var(--event-1)"><h3>EVENT 1</h3><p>24-08-2016, 05.30 PM<br>RIDGELINE HALL, NEW YORK</p></div>
<div class="event" style="left:405px;width:383px;background:var(--event-2)"><h3>EVENT 2</h3><p>24-08-2016, 05.30 PM<br>RIDGELINE HALL, NEW YORK</p></div>
<div class="event" style="left:801px;width:399px;background:var(--event-3)"><h3>EVENT 3</h3><p>24-08-2016, 05.30 PM<br>RIDGELINE HALL, NEW YORK</p></div>

<section class="press">
  <div class="press-badge"></div><div class="press-badge"></div><div class="press-badge"></div><div class="press-badge"></div>
</section>

<footer class="footer">
  <svg class="abs" style="left:30px;top:58px" width="24" height="32" viewBox="0 0 24 32"><path d="M12 0C5.4 0 0 5.3 0 11.8 0 20.6 12 32 12 32s12-11.4 12-20.2C24 5.3 18.6 0 12 0zm0 16a4.3 4.3 0 1 1 0-8.6 4.3 4.3 0 0 1 0 8.6z" fill="#fff"/></svg>
  <div class="abs label" style="left:80px;top:56px">OFFICE:</div>
  <div class="abs value" style="left:80px;top:92px">4180 N Mesa Vista Rd,<br>Suite 210<br>Phoenix, AZ 85018</div>

  <svg class="abs" style="left:740px;top:58px" width="28" height="28" viewBox="0 0 24 24"><path d="M6.6 10.8a15.1 15.1 0 0 0 6.6 6.6l2.2-2.2c.3-.3.7-.4 1-.2 1.1.4 2.3.6 3.6.6.6 0 1 .4 1 1V20c0 .6-.4 1-1 1A17 17 0 0 1 3 4c0-.6.4-1 1-1h3.5c.6 0 1 .4 1 1 0 1.3.2 2.5.6 3.6.1.3 0 .7-.2 1z" fill="#fff"/></svg>
  <div class="abs label" style="left:797px;top:56px">PHONE NUMBER:</div>
  <div class="abs value" style="left:797px;top:92px">+1 (866) 555-0142</div>

  <svg class="abs" style="left:740px;top:200px" width="30" height="24" viewBox="0 0 30 24"><rect x="1.5" y="1.5" width="27" height="21" rx="2" fill="none" stroke="#fff" stroke-width="3"/><path d="M2 3l13 10L28 3" fill="none" stroke="#fff" stroke-width="3"/></svg>
  <div class="abs label" style="left:797px;top:194px">EMAIL:</div>
  <div class="abs value" style="left:797px;top:230px">info@harrowmintwork.com</div>

  <div class="follow-bar">
    <span>FOLLOW US:</span>
    <span class="dot"></span><span class="dot"></span><span class="dot"></span><span class="dot"></span><span class="dot"></span>
  </div>
</footer>

</body>
</html>
```